Oil and Gas Exploration and Production company needs a business card design

We need a business card design using our logo and colors in the logo. We want a mainstream design.

```html
<!DOCTYPE html>
<html lang="en">
<head>
<meta charset="utf-8">
<title>Soltera Oil &amp; Gas – Business Card</title>
<link rel="stylesheet" href="https://fonts.googleapis.com/css2?family=Crimson+Pro:wght@400;600;700&display=swap">
<style>
  :root {
    --page-bg: #ececec;
    --card-white: #fbfbfb;
    --ink-black: #070708;
    --brand-gold: #d19a2c;
    --text-white: #ffffff;
  }
  * { box-sizing: border-box; margin: 0; padding: 0; }
  html, body {
    width: 1200px;
    height: 586px;
    overflow: hidden;
    background: var(--page-bg);
  }
  .canvas {
    position: relative;
    width: 1200px;
    height: 586px;
  }
  .business-card {
    position: absolute;
    left: 170px;
    top: 35px;
    width: 860px;
    height: 516px;
    background: var(--card-white);
    font-family: "Crimson Pro", Georgia, serif;
  }
  .brand-lockup {
    position: absolute;
    left: 0;
    right: 0;
    top: 52px;
    display: flex;
    align-items: center;
    justify-content: center;
    gap: 22px;
  }
  .brand-dot {
    width: 64px;
    height: 64px;
    border-radius: 50%;
    background: var(--brand-gold);
    flex: none;
  }
  .brand-name {
    color: var(--ink-black);
    font-weight: 700;
    line-height: 0.95;
  }
  .brand-name .brand-main {
    display: block;
    font-size: 122px;
    letter-spacing: -1px;
  }
  .brand-name .brand-sector {
    display: block;
    font-size: 40px;
    letter-spacing: 9px;
    text-align: right;
    margin-top: 4px;
  }
  .contact-band {
    position: absolute;
    left: 21px;
    top: 274px;
    width: 819px;
    height: 220px;
    background: var(--ink-black);
    border-radius: 38px;
  }
  .identity {
    position: absolute;
    right: 480px;
    top: 58px;
    text-align: right;
  }
  .person-name {
    color: var(--brand-gold);
    font-weight: 700;
    font-size: 21px;
    line-height: 1.2;
  }
  .person-title {
    color: var(--text-white);
    font-size: 17px;
    line-height: 1.3;
  }
  .office-address {
    margin-top: 12px;
    color: var(--brand-gold);
    font-weight: 700;
    font-size: 18px;
    line-height: 1.55;
    font-style: normal;
  }
  .divider {
    position: absolute;
    left: 380px;
    top: 59px;
    width: 3px;
    height: 116px;
    background: var(--text-white);
  }
  .contact-list {
    position: absolute;
    left: 418px;
    top: 66px;
    list-style: none;
  }
  .contact-item {
    display: flex;
    align-items: center;
    height: 35px;
    color: var(--text-white);
    font-size: 18px;
  }
  .contact-icon {
    width: 18px;
    height: 18px;
    margin-right: 15px;
    flex: none;
    fill: var(--brand-gold);
  }
  .contact-dot {
    width: 15px;
    height: 15px;
    margin: 0 19px 0 2px;
    border-radius: 50%;
    background: var(--brand-gold);
    flex: none;
  }
</style>
</head>
<body>
<main class="canvas">
  <section class="business-card">
    <header class="brand-lockup">
      <span class="brand-dot" aria-hidden="true"></span>
      <h1 class="brand-name">
        <span class="brand-main">Soltera</span>
        <span class="brand-sector">OIL &amp; GAS</span>
      </h1>
    </header>

    <div class="contact-band">
      <div class="identity">
        <p class="person-name">Marissa Holt</p>
        <p class="person-title">Chief Executive Offer</p>
        <address class="office-address">4150 Ridgeway Blvd<br>Suite 210, NC 27560</address>
      </div>

      <span class="divider" aria-hidden="true"></span>

      <ul class="contact-list">
        <li class="contact-item">
          <svg class="contact-icon" viewBox="0 0 24 24" aria-hidden="true">
            <path d="M3 8c0-2 4-4 9-4s9 2 9 4v2h-5V8.5c-1-.5-2.5-.7-4-.7s-3 .2-4 .7V10H3z"/>
            <path d="M7 11h10l3 8H4z"/>
          </svg>
          919.555.0148
        </li>
        <li class="contact-item">
          <svg class="contact-icon" viewBox="0 0 24 24" aria-hidden="true">
            <path d="M2 5h20v14H2z M4 7v.5l8 5.5 8-5.5V7z" fill-rule="evenodd"/>
          </svg>
          919.555.0193
        </li>
        <li class="contact-item">
          <span class="contact-dot" aria-hidden="true"></span>
          mholt@soltera-energy.com
        </li>
      </ul>
    </div>
  </section>
</main>
</body>
</html>
```